Blood Testing Health App

We are looking for a graphics designer to create a web app for us so that we may insert it into a health management website system.
For branding purposes we are at www.Veritamed.com and we are revamping our website... Example of new colors attached.
How we work...
We are a blood testing company based in the USA.
We offer a blood testing service nationwide in the USA.
We allow customers to order tests directly from us, visit a lab, have their blood drawn, or submit a urine sample, the lab tests it and they send the results back to our computer system and we share it with the customer.
The benefits of this are the customer does not need to go to the doctor and pay for the doctors visit to order these tests, which save them money. The tests are cheaper than going through the doctor. The customer simply uses us to get the test and the results and they can then take the results to their doctor... this process has saved them money. Others may be interested in regular check ups for blood work etc... and this allows them to do it with out needing a doctor, or if you have no insurance, this is a cheaper option too. We are quicker than a doctor, customers do not need appointments etc.
Hopefully you now have a better understanding as to what we do.
Here is the spec.
The app screen size is 750 px wide by 700 px high. ( A pdf is attached to show where the app is going to go, it is on page 3 of the pdf) The customer will have the ability to scroll… therefore the length of the page can be longer.
The app will consist of the following sections
Entry Page –
This will be the first page the user sees upon opening the app. This will be where they are directed from to the sections of the app discussed below. This needs to be branded for VeritaMed with a modern look.
1 – Order Test (Giving them the ability to purchase a blood test within the app)
2 – VeritaMed Dashboard (A dashboard that has everything they could need to use our service_
How it works Section on entry page – this will be a simple set of graphics showing how the service works. We already have the graphics for this, they do not need to be built again. They are attached to this brief
Basic structure of sections –
Order Test –
This page contains all tests, filed in categories – and Sub categories – Each test needs a link to an Information section – Price – Buy Now – Cart Process
VeritaMed Dashboard –
A page of icons along the top of the app
- My Confirmation
- My Nearest Lab
- My Receipt
- My Orders
- My Account
- My Results
- My Inbox
- Contact Us
Sections in more detail -
Order A Test –
Show all categories/ sub categories – There are 23 categories, 14 sub categories, and within these categories are 300 tests - Here is the information for the categories etc - http://www.veritamed.com/panels.aspx?PanelGroupID=4 Just in case it helps :)
We need to present this in a graphic format that is spacious, modern (quillbox, taskhub web appearance is the direction we are going for) We need it to be clear and not overwhelming to the customer.
Functionality idea…
Customer clicks category/ subcategory and tests appear.
Customer sees small 35 word description. For more information the test opens into a lightbox or expand the container which ever graphic designer believes to be most visually appealing
Buy Now must always be visible, along with price of the test
Buying process explained – Customer clicks buy now –
They are then taken to a Review Order screen ( This contains Order summary and choose payment method – insert payment details )
– Confirm payment –
Confirmation screen appears, thanking them.
They are then taken to the VeritaMed Dashboard...
VeritaMed Dashboard –
"My Confirmation" - Print Confirmation Order (PDF is in brief, we want this web based not a pdf download)
"My Nearest Lab Location" - This does not need to be designed because the web developer has this part under control, but we do need the icon in the dashboard
"My Receipt" - Print receipt - This does not exist in our system yet. So we need to create this from scratch - It will need to have - The test they are purchasing and the amount of the test - The customers name - The order ID - Must provide printer friendly option too
"My Orders" - This will have a list of orders - At the end of each order will be a status update of either "Test results" "Open order"
A graphic table format would be perfect. This will be linked to relevant results if they have been received. I have also attached a version of what the customer currently sees on our website. We know it is nasty ;) We are redesigning... but the information is there for this section to help design it with the right info. If the results are ready it will say in this list.
"Results Ready" will be a link to show those results once the customer has clicked the link, and the results will appear in the app, under the icons. There must be a printer friendly version too.
"My Results" Developer will sort this page out but we need the icon... It will be exactly like my orders but only show test results
"My Account" - This will be a place for them to update their personal information - Name, DOB, Address, Email Address
"My Inbox" - An inbox interface - Our way of contacting the customer for promotions we are running etc – We need a design of how this screen will appear. We also need the icon in the dashboard to have a notification on it if there are messages in the customers inbox. A little red 1, or circle with number of messages in the inbox.
"Customer Service" - This does not need to be designed because the web developer has this part under control, but we do need the icon in the dashboard
Icons appear along the top of app ( example - Mac icons/ iphone app icons) When the customer clicks an icon the content always appears below the icons
Here is more information for the icons and what should appear when each icon is clicked.
Screens to be designed –
Entry Page
Order A Test Page
Review Order Screen/Payment Screen - Show a lightbox that shows payment has been confirmed. Customer clicks close and are on the Confirmation Screen
VeritaMed Dashboard - Screens mentioned in detail above
We can't wait to see your designs!
Please email any questions.
Hi all this is the first time we have used pixel forum and understand the budget was too low for this project. We have now increased the budget to $2,000 and extended the deadline by another week
Hi all we are receiving some really great designs. I just added an example of the space that the web app will be going into... It is called "kelvraapp.pdf"
Hi guys updated the brief. Hopefully this will help with the dashboard part of the design

```html
<!DOCTYPE html>
<html lang="en">
<head>
<meta charset="utf-8">
<title>VeritaMed – Shopping Cart</title>
<link rel="stylesheet" href="https://fonts.googleapis.com/css2?family=Open+Sans:ital,wght@0,400;0,600;1,400&display=swap">
<style>
  :root {
    --brand-green: #8ca600;
    --title-green: #7d9a00;
    --page-bg: #f6f4f5;
    --text-dark: #333333;
    --row-border: #9bb520;
    --footer-brown: #3b1706;
    --logo-ink: #2a1a08;
    --white: #ffffff;
    --input-border: #8a8a8a;
  }
  * { margin: 0; padding: 0; box-sizing: border-box; }
  html, body { width: 692px; height: 1200px; overflow: hidden; }
  body {
    position: relative;
    background: var(--page-bg);
    font-family: "Open Sans", "Segoe UI", sans-serif;
    color: var(--text-dark);
  }
  .site-header {
    position: absolute; left: 0; top: 0; width: 692px; height: 118px;
    background: var(--brand-green);
    display: flex; align-items: center; justify-content: center; gap: 12px;
  }
  .brand-mark { width: 26px; height: 26px; background: var(--logo-ink); opacity: .55; }
  .brand-name { font-size: 40px; font-weight: 400; color: var(--logo-ink); letter-spacing: .5px; }

  .cart-title {
    position: absolute; left: 0; top: 138px; width: 692px; text-align: center;
    font-size: 31px; font-weight: 400; color: var(--title-green);
  }
  .cart-intro {
    position: absolute; left: 39px; top: 188px; width: 620px;
    font-size: 23.5px; line-height: 29.5px;
  }

  .cart-table {
    position: absolute; left: 34px; top: 360px; width: 623px; height: 360px;
    border: 1.5px solid var(--row-border); background: var(--page-bg);
  }
  .cart-head {
    height: 47px; background: var(--brand-green); color: var(--white);
    font-size: 25px; position: relative;
  }
  .cart-head span { position: absolute; top: 5px; }
  .col-name { left: 16px; }
  .col-price { left: 294px; }
  .cart-row {
    position: relative; height: 54px; background: var(--white);
    border-bottom: 1.5px solid var(--row-border); font-size: 16.5px;
  }
  .item-name { position: absolute; left: 8px; top: 9px; }
  .item-detail { position: absolute; left: 19px; top: 32px; font-size: 12px; color: var(--title-green); }
  .cart-row.second .item-detail { left: 16px; top: 30px; }
  .item-price { position: absolute; left: 306px; top: 9px; }
  .item-remove { position: absolute; left: 459px; top: 9px; }

  .coupon-input {
    position: absolute; left: 30px; top: 191px; width: 552px; height: 57px;
    background: var(--white); border: 1px solid var(--input-border);
  }
  .coupon-button {
    position: absolute; left: 163px; top: 270px; width: 286px; height: 46px;
    background: linear-gradient(#8fab08, #6f8c00);
    color: var(--white); font-size: 25.5px; text-align: center; line-height: 46px;
    box-shadow: 0 1px 2px rgba(0,0,0,.3); text-shadow: 0 1px 1px rgba(0,0,0,.35);
  }

  .order-notes {
    position: absolute; left: 49px; top: 853px; width: 610px;
    font-size: 20.5px; line-height: 26.6px; font-style: italic;
  }
  .order-notes p + p { margin-top: 26px; }

  .cart-actions {
    position: absolute; left: 0; top: 1128px; width: 692px; height: 72px;
    background: var(--footer-brown); color: var(--white);
    display: flex; align-items: center; justify-content: center; gap: 14px;
    font-size: 22px;
  }
  .cart-actions .divider { font-size: 20px; }
</style>
</head>
<body>
  <header class="site-header">
    <div class="brand-mark"></div>
    <div class="brand-name">VeritaMed</div>
  </header>

  <h1 class="cart-title">Contents of Your Shopping Cart</h1>
  <p class="cart-intro">This site uses financial encryption for secure payment processing. By clicking the "Secure Checkout" button below you may pay for your order with a credit card or through your PayWell account.</p>

  <section class="cart-table">
    <div class="cart-head">
      <span class="col-name">Item Name</span>
      <span class="col-price">Price</span>
    </div>
    <div class="cart-row">
      <span class="item-name">Amenorrhea Profile</span>
      <span class="item-detail">Show Detail</span>
      <span class="item-price">$105.00</span>
      <span class="item-remove">Remove from Cart</span>
    </div>
    <div class="cart-row second">
      <span class="item-name">Amenorrhea Profile</span>
      <span class="item-detail">Show Detail</span>
      <span class="item-price">$105.00</span>
      <span class="item-remove">Remove from Cart</span>
    </div>
    <div class="coupon-input"></div>
    <div class="coupon-button">Apply Coupon Code</div>
  </section>

  <section class="order-notes">
    <p>Once you have ordered your test, you can select from over 1,700 Clinora locations around the country. Remember, the average time for results is two to three days.</p>
    <p>You will receive an email from us informing you that your information is available in your private account. Log in to view your results in a convenient PDF format. Any abnormal results will be highlighted.</p>
  </section>

  <nav class="cart-actions">
    <span>Secure Checkout</span><span class="divider">I</span>
    <span>Empty Shopping Cart</span><span class="divider">I</span>
    <span>Continue Shopping</span>
  </nav>
</body>
</html>
```